Boutique town planning business needs a Business Card design

We need a business card design for a new company called The Zoning Bridgeway. We provide town planning and urban design services to government, business and community groups. We would like to see the designs use the colours in the logo (blue, deep red, green and amber), plenty of white and including black and grey in the writing. The final design should communicate collaboration, creativity and professionalism and that we are approachable.

```html
<!DOCTYPE html>
<html lang="en">
<head>
<meta charset="utf-8">
<title>The Zoning Bridgeway – Business Card</title>
<link rel="stylesheet" href="https://fonts.googleapis.com/css2?family=Exo+2:wght@400;500;700&display=swap">
<style>
  :root {
    --stage: #e9e9e9;
    --card-white: #ffffff;
    --card-black: #0d0d0d;
    --ink-light: #ffffff;
    --ink-dark: #2b2b2b;
    --ink-grey: #5a5a5a;
    --brand-blue: #2f8fc4;
  }
  html, body {
    margin: 0;
    width: 1200px;
    height: 1085px;
    overflow: hidden;
    background: var(--stage);
    font-family: "Exo 2", sans-serif;
  }
  .card {
    position: absolute;
    left: 110px;
    top: 262px;
    width: 980px;
    height: 560px;
    background: var(--card-white);
    box-shadow: 0 12px 30px rgba(0,0,0,0.18);
    overflow: hidden;
  }
  .contact-panel {
    position: absolute;
    inset: 0;
    width: 980px;
    height: 560px;
  }
  .contact-list {
    position: absolute;
    left: 0;
    top: 0;
    width: 528px;
    height: 560px;
    margin: 0;
    padding: 0;
    list-style: none;
    color: var(--ink-light);
    text-align: right;
    font-size: 30px;
    line-height: 1.22;
    letter-spacing: 1px;
  }
  .contact-item {
    position: absolute;
    right: 0;
    width: 460px;
  }
  .contact-item--phone { top: 95px; }
  .contact-item--address { top: 230px; }
  .contact-item--web { top: 378px; }
  .identity {
    position: absolute;
    left: 660px;
    top: 150px;
    width: 300px;
  }
  .brand {
    display: flex;
    align-items: center;
    gap: 14px;
    margin-bottom: 70px;
  }
  .brand-dot {
    width: 54px;
    height: 54px;
    border-radius: 50%;
    background: var(--brand-blue);
    flex: none;
  }
  .brand-name {
    font-size: 30px;
    font-weight: 700;
    line-height: 1.05;
    color: var(--ink-dark);
  }
  .person-name {
    margin: 0;
    font-size: 32px;
    font-weight: 500;
    letter-spacing: 2px;
    color: var(--ink-dark);
    white-space: nowrap;
  }
  .person-role {
    margin: 4px 0 0;
    font-size: 26px;
    color: var(--ink-grey);
    letter-spacing: 1px;
  }
</style>
</head>
<body>
  <div class="card">
    <svg class="contact-panel" viewBox="0 0 980 560" aria-hidden="true">
      <path fill="#0d0d0d" d="M0 0 H548 V60
        C548 80 625 80 625 115 C625 150 548 150 548 170
        V195 C548 215 625 215 625 250 C625 285 548 285 548 305
        V343 C548 363 625 363 625 398 C625 433 548 433 548 453
        V560 H0 Z"/>
      <g fill="none" stroke="#ffffff" stroke-width="3">
        <circle cx="584" cy="115" r="26"/>
        <circle cx="584" cy="250" r="26"/>
        <circle cx="584" cy="398" r="26"/>
      </g>
      <path fill="#ffffff" d="M573 104 c3-3 6-2 7 1 l2 5 c1 2 0 4-2 5 l-2 1 c2 4 5 7 9 9 l1-2 c1-2 3-3 5-2 l5 2 c3 1 4 4 1 7 c-3 3-7 4-11 2 c-8-4-14-10-18-18 c-2-4-1-8 3-10 Z"/>
      <path fill="#ffffff" fill-rule="evenodd" d="M584 234 c-8 0-13 6-13 13 c0 9 13 21 13 21 s13-12 13-21 c0-7-5-13-13-13 Z M584 243 a5 5 0 1 1 0 10 a5 5 0 1 1 0-10 Z"/>
      <g fill="none" stroke="#ffffff" stroke-width="2">
        <circle cx="584" cy="398" r="14"/>
        <ellipse cx="584" cy="398" rx="6" ry="14"/>
        <line x1="570" y1="398" x2="598" y2="398"/>
        <line x1="573" y1="390" x2="595" y2="390"/>
        <line x1="573" y1="406" x2="595" y2="406"/>
      </g>
    </svg>
    <ul class="contact-list">
      <li class="contact-item contact-item--phone">012 555 0147<br>012 555 0147</li>
      <li class="contact-item contact-item--address">027 4th floor,<br>Harbour Lane Road<br>NDV</li>
      <li class="contact-item contact-item--web">info@zbway.com<br>www.zbway.com</li>
    </ul>
    <div class="identity">
      <div class="brand">
        <span class="brand-dot"></span>
        <span class="brand-name">The Zoning<br>Bridgeway</span>
      </div>
      <p class="person-name">MARTIN CALLOWAY</p>
      <p class="person-role">Managing Director</p>
    </div>
  </div>
</body>
</html>
```